Internet Of Things brochure

Need to create a brochure with a common theme to our website and the last 2 pages of the attached file. All the contect is in the file that I have attached.
website www.norvalenetworks.com.au

Industry/Entity Type

Internet

```html
<!DOCTYPE html>
<html lang="en">
<head>
<meta charset="utf-8">
<title>Norvale Networks – Digital Discovery Brochure</title>
<link href="https://fonts.googleapis.com/css2?family=Oswald:wght@400;500&family=Rubik:ital,wght@0,400;0,500;0,700;1,700&display=swap" rel="stylesheet">
<style>
:root{
  --page:#e6e7e9;
  --paper:#f1f2f5;
  --ink:#2b2f38;
  --body:#4a4f5a;
  --blue:#3a8fd9;
  --blue-light:#62aee8;
  --blue-pale:#9dcdf2;
  --navy:#1f2a3c;
  --slate:#5d6268;
  --grey-tri:#c8ccd4;
}
*{box-sizing:border-box;margin:0;padding:0}
html,body{width:835px;height:1200px;overflow:hidden;background:var(--page)}
body{font-family:"Rubik",sans-serif;color:var(--body);position:relative}
.spread{position:absolute;left:20px;width:795px;height:550px;background:var(--paper);overflow:hidden;box-shadow:0 2px 8px rgba(0,0,0,.12)}
.spread--outside{top:25px}
.spread--inside{top:620px}
.spread__art{position:absolute;inset:0;width:795px;height:550px}
.fold{position:absolute;top:0;left:397px;width:1px;height:550px;background:rgba(0,0,0,.06)}
.abs{position:absolute}
.heading{font-family:"Rubik",sans-serif;font-weight:700;font-style:italic;font-size:15px;line-height:1.1;color:var(--ink);text-transform:uppercase}
.heading .accent{display:block;color:var(--blue)}
.body-copy{font-size:7.6px;line-height:1.5;color:var(--body)}
.body-copy p+p{margin-top:4px}
.body-copy--tight{line-height:1.42}
.body-copy--tight p+p{margin-top:3px}
.brand{font-family:"Rubik",sans-serif;font-weight:700;color:var(--navy);display:flex;align-items:center;gap:6px}
.brand__dot{width:12px;height:12px;background:var(--blue);display:inline-block}
.badges{display:flex;gap:14px;align-items:center}
.badge{width:42px;height:22px;background:#d5dbe4;border-radius:3px}
.badge--blue{background:var(--blue-light)}
.contacts{list-style:none;font-size:8px;line-height:1.35;color:var(--ink);font-weight:500}
.contacts li{display:flex;gap:8px;align-items:flex-start;margin-bottom:6px}
.contacts svg{flex:none;width:10px;height:10px;margin-top:1px}
.headline{font-family:"Oswald",sans-serif;font-weight:400;font-size:27px;line-height:1.08;color:var(--ink);text-transform:uppercase;text-align:right}
.headline .accent{color:var(--blue)}
.talk{font-size:8px;text-align:right;color:var(--ink)}
.talk strong{display:block;font-size:13px;font-weight:500}
.web{font-family:"Rubik",sans-serif;font-size:9px;letter-spacing:2px;color:#fff}
.ask{font-size:7.6px;line-height:1.45}
.ask dt{font-weight:700;color:var(--ink);margin-bottom:3px}
.ask dd{color:var(--blue);padding-left:8px;position:relative;margin-bottom:2px}
.ask dd::before{content:"";position:absolute;left:0;top:4px;width:4px;height:4px;background:var(--navy)}
.services{display:flex;gap:12px;align-items:flex-start}
.service{width:82px}
.service__pill{background:var(--blue-light);color:#fff;font-size:7px;line-height:1.2;border-radius:9px;text-align:center;padding:3px 4px;margin-bottom:4px}
.service ul{list-style:none;font-size:6.8px;line-height:1.25;color:var(--ink)}
.service li::before{content:"• ";color:var(--blue)}
.web-pill{background:var(--blue-pale);border-radius:10px;text-align:center;padding:4px 0}
.web-pill .web{color:#fff}
.web-bar{background:rgba(20,24,32,.85);border-radius:0 10px 10px 0;padding:5px 14px}
</style>
</head>
<body>

<section class="spread spread--outside" aria-label="Brochure outside spread">
  <svg class="spread__art" viewBox="0 0 795 550">
    <defs>
      <linearGradient id="blueBand" x1="0" y1="0" x2="1" y2="1">
        <stop offset="0" stop-color="#5eaeea"/>
        <stop offset="1" stop-color="#2f7fcf"/>
      </linearGradient>
      <linearGradient id="darkPanel" x1="0" y1="0" x2="0" y2="1">
        <stop offset="0" stop-color="#3a4558"/>
        <stop offset="1" stop-color="#1c2432"/>
      </linearGradient>
      <linearGradient id="meetingPhoto" x1="0" y1="0" x2="1" y2="1">
        <stop offset="0" stop-color="#2f6f9d"/>
        <stop offset="1" stop-color="#183049"/>
      </linearGradient>
      <linearGradient id="officePhoto" x1="0" y1="0" x2="1" y2="0">
        <stop offset="0" stop-color="#4a5566"/>
        <stop offset="1" stop-color="#c9ced6"/>
      </linearGradient>
    </defs>
    <polygon points="0,25 150,25 110,105 0,105" fill="url(#officePhoto)" role="img" aria-label="Photo of two businessmen reviewing a tablet"/>
    <polygon points="150,25 240,25 150,105" fill="var(--grey-tri)"/>
    <polygon points="210,0 520,0 600,215 545,260 397,165" fill="url(#blueBand)"/>
    <polygon points="397,165 545,260 455,550 300,550 345,300" fill="url(#darkPanel)"/>
    <polygon points="545,260 795,300 795,550 455,550" fill="url(#meetingPhoto)" role="img" aria-label="Photo of a team meeting around a boardroom table, tinted blue"/>
    <polygon points="795,262 795,335 735,300" fill="var(--grey-tri)" opacity=".8"/>
    <rect x="0" y="536" width="300" height="14" fill="var(--blue-light)"/>
  </svg>

  <div class="abs" style="left:32px;top:125px;width:330px">
    <h2 class="heading" style="font-size:14px;font-style:normal"><span class="accent">Request a Digital</span>Discovery Workshop</h2>
    <div class="body-copy" style="margin-top:8px">
      <p>The Digital Discovery Workshop is a half-day opportunity for the key stakeholders of your business that allows Norvale Digital to identify and explore which areas of your business are best suited to a digital transformation. During this workshop you will also learn about the threats that the digital environment may pose to your business specifically, and the opportunities and possibilities that exist by applying digital solutions to your existing business. We also provide our clients with the opportunity to consider the overall strategy and actions needed within their organisation to help them develop a competitive advantage inside the context of the ever-changing digital business environment. This analysis is relevant to all business types and industries.</p>
    </div>
  </div>

  <div class="badges abs" style="left:150px;top:318px" aria-label="Partner badges">
    <span class="badge"></span><span class="badge badge--blue"></span><span class="badge"></span>
  </div>

  <div class="brand abs" style="left:32px;top:365px;font-size:14px"><span class="brand__dot"></span>Norvale Networks</div>

  <ul class="contacts abs" style="left:32px;top:395px;width:260px">
    <li><svg viewBox="0 0 10 10"><path d="M5 0.5a3 3 0 0 1 3 3c0 2.3-3 6-3 6s-3-3.7-3-6a3 3 0 0 1 3-3z" fill="var(--navy)"/><circle cx="5" cy="3.5" r="1.1" fill="#fff"/></svg><span>Kelmoor Head Office 18-22 Arden Road<br>Kelmoor, NSW, 2190</span></li>
    <li><svg viewBox="0 0 10 10"><path d="M5 0.5a3 3 0 0 1 3 3c0 2.3-3 6-3 6s-3-3.7-3-6a3 3 0 0 1 3-3z" fill="var(--navy)"/><circle cx="5" cy="3.5" r="1.1" fill="#fff"/></svg><span>Sales Office<br>41 Harbourline Way, Sydney NSW 2000</span></li>
    <li><svg viewBox="0 0 10 10"><path d="M2 1l2 0 1 2.5-1.2 1a5 5 0 0 0 2.7 2.7l1-1.2L10 7v2c-4.5 .5-9-4-8.5-8z" fill="none" stroke="var(--navy)" stroke-width=".9"/></svg><span>1300 614 207</span></li>
    <li><svg viewBox="0 0 10 10"><rect x=".5" y="2" width="9" height="6" fill="none" stroke="var(--navy)" stroke-width=".9"/><path d="M.5 2l4.5 3.5L9.5 2" fill="none" stroke="var(--navy)" stroke-width=".9"/></svg><span>hello@norvalenetworks.com.au</span></li>
    <li><svg viewBox="0 0 10 10"><circle cx="5" cy="5" r="4.3" fill="none" stroke="var(--navy)" stroke-width=".9"/><path d="M.7 5h8.6M5 .7c-2.2 2.5-2.2 6.1 0 8.6M5 .7c2.2 2.5 2.2 6.1 0 8.6" fill="none" stroke="var(--navy)" stroke-width=".7"/></svg><span>www.norvalenetworks.com.au</span></li>
  </ul>

  <div class="brand abs" style="left:580px;top:38px;font-size:16px"><span class="brand__dot"></span>Norvale Networks</div>
  <h1 class="headline abs" style="right:40px;top:80px;width:220px">Interested in<br>discovering<br>your digital<br><span class="accent">opportunities?</span></h1>
  <div class="talk abs" style="right:40px;top:218px;border-top:1px solid var(--ink);padding-top:4px;width:90px">Let's Talk :<strong>1300 614 207</strong></div>
  <div class="web abs" style="right:40px;top:505px">www.norvalenetworks.com.au</div>
  <div class="fold"></div>
</section>

<section class="spread spread--inside" aria-label="Brochure inside spread">
  <svg class="spread__art" viewBox="0 0 795 550">
    <defs>
      <linearGradient id="tabletPhoto" x1="0" y1="0" x2="1" y2="1">
        <stop offset="0" stop-color="#6a5a4c"/>
        <stop offset="1" stop-color="#241d19"/>
      </linearGradient>
      <linearGradient id="teamPhoto" x1="0" y1="0" x2="1" y2="0">
        <stop offset="0" stop-color="#dfe3e8"/>
        <stop offset="1" stop-color="#8a95a5"/>
      </linearGradient>
    </defs>
    <polygon points="0,255 95,315 0,385" fill="var(--slate)"/>
    <polygon points="0,425 120,412 240,470 215,550 0,550" fill="url(#tabletPhoto)" role="img" aria-label="Photo of a hand holding a tablet showing a business presentation"/>
    <polygon points="250,550 330,445 397,470 397,550" fill="var(--blue)"/>
    <polygon points="650,0 795,0 795,200 690,200" fill="url(#teamPhoto)" role="img" aria-label="Photo of business colleagues discussing a report at a desk"/>
    <polygon points="795,200 795,290 745,200" fill="var(--slate)"/>
  </svg>

  <div class="abs" style="left:30px;top:22px;width:340px">
    <h2 class="heading">Embrace digital or<span class="accent">risk being left behind</span></h2>
    <div class="body-copy" style="margin-top:8px">
      <p>Does your business have the Digital DNA required to succeed in the digital era?</p>
      <p>Embracing the new revolution in digital technology is more than just having an eCommerce website. It's about what is possible when every aspect of your business harnesses the power of digital innovation. When the sum of your business parts are digital and linked together, your business can completely transform through being more effective, productive and automated.</p>
      <p>The way businesses operate has forever been changed by advancements in digital technology. Integrated systems allow for sophisticated eCommerce, automated business operations, digital marketing, CRMs and learning &amp; development opportunities. These can be connected together so that digital businesses now operate with an agility and efficiency that traditional business models don't or can't adapt.</p>
      <p>Many enterprises have failed to adapt to this change. Through not integrating their business into the digital ecosystem, it exposes them to the possibility of failing to properly engage with their customers.</p>
    </div>
  </div>

  <div class="abs" style="left:110px;top:238px;width:270px">
    <h2 class="heading">The age of digital<span class="accent">disruption is here</span></h2>
    <div class="body-copy" style="margin-top:8px">
      <p>The world's largest taxi firm, Rydeo, owns no vehicles. The world's largest accommodation provider, Stayhive, owns no real estate. The world's biggest phone companies, Callora and Chatloop, own no telco infrastructure. The world's most valuable retailer, Tradora, has no stock. The most popular media company, Friendscape, creates no content. The world's largest movie house, Streamvale, owns no cinemas. Something big has happened. It's called digital disruption.</p>
      <p>Creating and controlling the marketplace between the consumer and the provider of the goods or services is now the most valuable place to be. This is where risk is low, costs are slashed and profits are maximised. This digital revolution poses both a significant threat and a significant opportunity.</p>
    </div>
  </div>

  <div class="web-bar abs" style="left:0;top:505px"><span class="web">www.norvalenetworks.com.au</span></div>

  <dl class="ask abs" style="left:425px;top:20px;width:200px">
    <dt>So ask yourself :</dt>
    <dd>Is your business capable of responding quickly to digital threats?</dd>
    <dd>Are you doing all you can to compete in the digital business environment?</dd>
    <dd>Are you considering alternative business models and opportunities available through digitization?</dd>
    <dd>Does your business continue to grow in value in the face of digital threats?</dd>
  </dl>

  <div class="body-copy abs" style="left:425px;top:124px;width:235px">
    <p>Norvale Digital works closely with you to identify and focus on the valuable digital opportunities available to your business operation, re-design your processes and prepare your business for the task of competing in the global digital environment. Partner with us and you'll discover what is possible for your business – and how you can take your business to another level.</p>
  </div>

  <div class="abs" style="left:425px;top:212px;width:335px">
    <h2 class="heading">The age of digital<span class="accent">disruption is here</span></h2>
    <div class="body-copy body-copy--tight" style="margin-top:6px">
      <p>Our digital solutions are varied – impacting all parts of the business model and are completely tailored to your business and your industry. <strong style="color:var(--ink)">We can cover the following scenarios (and more):</strong></p>
      <p>a) Introduce a digitally strategic business model digitising operations and processes by leveraging cloud-based applications and mobile devices that digitise data collection and collation and supply chain processes.<br>b) Learning &amp; Development solutions that comprise an array of digitised approaches that are always available on the Cloud, can be built in minutes, are completely customisable, are easy to maintain and are mobile friendly.<br>c) Seamlessly integrating digital commerce into your existing brick &amp; mortar business quickly, strategically and cost effectively – helping you compete.<br>d) Creating targeted and measurable digital marketing campaigns that focus on increasing first-time and repeat sales and building long-term customer loyalty.</p>
      <p><strong style="color:var(--ink)">How we're helping businesses reimagine their business through digital</strong></p>
    </div>
  </div>

  <div class="services abs" style="left:425px;top:428px">
    <div class="service"><div class="service__pill">Digital Commerce</div><ul><li>eCommerce</li><li>mCommerce</li><li>Digital payment integration</li><li>Logistics and Supply Chain integration</li></ul></div>
    <div class="service"><div class="service__pill">Digital Business Solutions</div><ul><li>Cloud ERP, CRM, SCM, HCM</li><li>Integration to ERP, CRM, SCM</li><li>Digital invoicing solutions</li><li>Any device ERP, CRM, SCM</li></ul></div>
    <div class="service"><div class="service__pill">Digital Marketing</div><ul><li>SEO &amp; SEM</li><li>Marketing insights &amp; analytics</li><li>Responsive EDMs and digital campaigns</li><li>Digital CTA</li><li>Proximity marketing</li></ul></div>
    <div class="service"><div class="service__pill">Digital Learning</div><ul><li>Cloud LMS</li><li>Learning &amp; Development solutions</li><li>Campus on Cloud</li></ul></div>
  </div>

  <div class="web-pill abs" style="left:470px;top:526px;width:260px"><span class="web">www.norvalenetworks.com.au</span></div>
  <div class="fold"></div>
</section>

</body>
</html>
```